This design will be for the label and logo of Dame Wren Tequila. The design needs to be on a bottle, using the primary color turquoise, white and navy blue. You can also use Burnt Orange or Light blue or another color that you think goes well with Turquoise. Dame Wren is a tequila that is inspired by a beachy, campy, coastal, ocean, nautical feel. It's a modern feeling brand. The text should simply say "Dame Wren Tequila" and also a logo or mark in or around the text. Please place the logo and lettering on a bottle (I have attached an example ) and put the other necessary details such as: 100% Agave, 750ml , 40% alc, 80 proof, Blanco Tequila. Dame Wren was a pirate, but we want her inspiration to be modern and not literal. I've attached some inspiration for the clean look we're going for.

Logo Text

Dame Wren Tequila

```html
<!DOCTYPE html>
<html lang="en">
<head>
<meta charset="utf-8">
<title>Dame Wren Tequila – Front Label</title>
<link href="https://fonts.googleapis.com/css2?family=Baloo+2:wght@700&family=Montserrat:wght@300&family=Allura&family=Oswald:wght@400;500&family=PT+Serif&display=swap" rel="stylesheet">
<style>
  :root {
    --backdrop: #000000;
    --label-paper: #efefeb;
    --turquoise: #4fd1c5;
    --turquoise-deep: #1f9a8e;
    --ink: #3a3a3a;
    --ink-soft: #5a5a5a;
  }
  html, body {
    margin: 0;
    padding: 0;
    overflow: hidden;
    background: var(--backdrop);
  }
  .canvas {
    position: relative;
    width: 1143px;
    height: 1200px;
    background: var(--backdrop);
    overflow: hidden;
  }
  .front-label {
    position: absolute;
    left: 131px;
    top: 85px;
    width: 880px;
    height: 1030px;
    background: var(--label-paper);
  }
  .front-label__frame {
    position: absolute;
    inset: 15px;
    border: 3px solid var(--turquoise);
  }
  .agave-claim {
    position: absolute;
    top: 80px;
    left: 0;
    width: 100%;
    text-align: center;
    font-family: "Montserrat", sans-serif;
    font-weight: 300;
    font-size: 46px;
    letter-spacing: 3px;
    color: var(--ink);
  }
  .agave-art {
    position: absolute;
    top: 230px;
    left: 294px;
    width: 292px;
    height: 230px;
    border-radius: 50% 50% 18px 18px;
    background: linear-gradient(180deg, var(--turquoise) 0%, var(--turquoise) 70%, var(--turquoise-deep) 100%);
  }
  .brand-name {
    position: absolute;
    top: 462px;
    left: 0;
    width: 100%;
    text-align: center;
    font-family: "Baloo 2", sans-serif;
    font-weight: 700;
    font-size: 150px;
    line-height: 1;
    color: var(--turquoise);
  }
  .spirit-type {
    position: absolute;
    top: 640px;
    left: 0;
    width: 100%;
    text-align: center;
    font-family: "Allura", cursive;
    font-size: 86px;
    line-height: 1;
    color: var(--ink);
  }
  .details {
    position: absolute;
    top: 820px;
    left: 0;
    width: 100%;
    height: 170px;
  }
  .details__col {
    position: absolute;
    top: 0;
    font-family: "Oswald", sans-serif;
    font-weight: 500;
    color: var(--ink-soft);
    text-align: center;
  }
  .details__col--volume { left: 145px; width: 125px; }
  .details__col--origin { left: 638px; width: 118px; }
  .details__top {
    font-size: 44px;
    line-height: 1;
    padding: 10px 0 12px;
    border-bottom: 2px solid var(--ink-soft);
  }
  .details__bottom {
    font-size: 34px;
    line-height: 1;
    padding-top: 14px;
  }
  .details__divider {
    position: absolute;
    top: 0;
    width: 6px;
    height: 160px;
    background: var(--ink-soft);
  }
  .details__divider--left { left: 281px; }
  .details__divider--right { left: 622px; }
  .details__center {
    position: absolute;
    top: 0;
    left: 305px;
    width: 300px;
    text-align: center;
    color: var(--ink-soft);
  }
  .grade {
    font-family: "PT Serif", serif;
    font-size: 50px;
    letter-spacing: 2px;
    line-height: 1.1;
  }
  .origin-line {
    display: flex;
    align-items: center;
    justify-content: center;
    gap: 6px;
    margin-top: 8px;
    font-family: "Oswald", sans-serif;
    font-size: 16px;
    line-height: 1;
  }
  .origin-line__text {
    border-top: 2px solid var(--ink-soft);
    border-bottom: 2px solid var(--ink-soft);
    padding: 3px 4px;
  }
  .origin-line__badge { display: block; }
  .distillery {
    margin-top: 12px;
    font-family: "Oswald", sans-serif;
    font-size: 20px;
    letter-spacing: 1px;
  }
</style>
</head>
<body>
<div class="canvas">
  <section class="front-label" aria-label="Dame Wren Tequila front label">
    <div class="front-label__frame"></div>

    <p class="agave-claim" style="margin:0">100% AGAVE</p>

    <div class="agave-art" role="img" aria-label="Turquoise agave plant illustration"></div>

    <h1 class="brand-name" style="margin:0">Dame Wren</h1>
    <p class="spirit-type" style="margin:0">Blanco Tequila</p>

    <div class="details">
      <div class="details__col details__col--volume">
        <div class="details__top">750ML</div>
        <div class="details__bottom">40% VOL</div>
      </div>
      <div class="details__divider details__divider--left"></div>

      <div class="details__center">
        <div class="grade">PREMIUM</div>
        <div class="origin-line">
          <span class="origin-line__text">PRODUCT OF</span>
          <svg class="origin-line__badge" width="70" height="36" viewBox="0 0 70 36" aria-hidden="true">
            <polygon points="35,2 68,18 35,34 2,18" fill="none" stroke="#5a5a5a" stroke-width="3"/>
          </svg>
          <span class="origin-line__text">IMPORTED</span>
        </div>
        <div class="distillery">UNKNOWN DISTILLERY</div>
      </div>

      <div class="details__divider details__divider--right"></div>
      <div class="details__col details__col--origin">
        <div class="details__top">USA</div>
        <div class="details__bottom">D.O.T. 166</div>
      </div>
    </div>
  </section>
</div>
</body>
</html>
```